Moulding supply company needs a Door Hanger Design

Door Hanger Design Request from Ledge Craft
www. ledgecrafts.ca
We are moulding factory outlet in Toronto. Provide high quality moulding materials with competitive price like crown mouldings, casings, wainscoting, flatstocks, baseboards. We also provide professional installation for our clients. This door hanger will help the home owner easily find a local factory supplier with providing the materials as well as installation.

Detail request for design:
Size: 4”x11”, vertical
Shape: Rectangle

Content:
Front
1. Logo, see attachment(Use the left one, horizontal one)
2. Moulding factory outlet direct sale
3. Supply high quality Crown mouldings, baseboards, casings and wainscotings with competitive price
4. Installation & delivery
#2 content is the most important content, should be bold and readable
#3 can be smaller font compare to #2

Address: 47 West Falcon Ridge Rd, Richmond Hill, ON L4C 2H8
Telephone: 416 555 0143
416 555 0178
Email: info@ledgecrafts.ca

Back
Slogan: Convert plain room into designer’s interiors

Telephone: 416 555 0143
416 555 0178
Email: info@ledgecrafts.ca

Images:
Front
1. Display our productions for crown mouldings, baseboards, casings and wainscotings, refer to our website www.ledgecrafts.ca. (The winner finally we will provide the high resolution images, low resolution please copy from our website so far)
Back
2. Display 4-6 nice images for 1. wainscoting walls 2. feature walls, 3. waffle ceiling like attached below. BUT PLEASE DON'T USE THE IMAGES PROVIDED, THIS IS ONLY A SAMPLE. Please use high resolution images for printing. ALSO PLEASE DON'T LIMIT YOUR CREATIVITY TO USE 4 SQUARES LIKE BELOW IMAGES. Please provide more ideas

Note:
1. Please do the bleeding for final printing production
2. Images have to be high resolution for ready to print
3. Style need to be fresh, clean, easy to read, modern and magazine style
4. Information has to be readable, easy to find, front and back both need to display company address, telephone, email, you can use icon or abbreviation to do these information.

Thanks,
Ledge Crafts

```html
<!DOCTYPE html>
<html lang="en">
<head>
<meta charset="utf-8">
<title>Ledge Crafts – Door Hanger</title>
<link rel="stylesheet" href="https://fonts.googleapis.com/css2?family=Oswald:wght@600;700&family=Lato:wght@400;700&family=Montserrat:wght@400&display=swap">
<style>
  :root {
    --brand-blue: #2350a3;
    --brand-orange: #f15a29;
    --paper: #ffffff;
    --ink: #111111;
    --stage: #4a494a;
    --photo-dark: #4a3f38;
    --photo-light: #d9d9d9;
  }
  * { margin: 0; padding: 0; box-sizing: border-box; }
  html, body { width: 1200px; height: 1200px; overflow: hidden; background: var(--stage); }
  .canvas { position: relative; width: 1200px; height: 1200px; }

  .hanger { position: absolute; top: 158px; width: 327px; height: 900px; overflow: hidden; }
  .hanger--front { left: 246px; }
  .hanger--back { left: 634px; }
  .hanger__bg { position: absolute; inset: 0; }

  .brand { position: absolute; left: 0; right: 0; display: flex; justify-content: center; align-items: center; gap: 10px; }
  .brand__mark { width: 24px; height: 24px; border: 2px solid var(--paper); }
  .brand__name { font-family: 'Montserrat', sans-serif; font-weight: 400; font-size: 26px; letter-spacing: 2px; color: var(--paper); white-space: nowrap; }
  .hanger--front .brand { top: 250px; }
  .hanger--back .brand { top: 232px; }

  .hero-photo { position: absolute; left: 0; top: 0; }

  .headline { position: absolute; left: 0; right: 0; text-align: center; font-family: 'Oswald', sans-serif; font-weight: 700; text-transform: uppercase; line-height: 1; }
  .headline--front { top: 590px; font-size: 37px; letter-spacing: 0.2px; }
  .headline--front .headline__line { display: block; }
  .headline__blue { color: var(--brand-blue); }
  .headline__orange { color: var(--brand-orange); margin-top: 1px; }

  .supply-copy { position: absolute; left: 24px; right: 20px; top: 672px; font-family: 'Lato', sans-serif; font-weight: 700; font-size: 15.5px; line-height: 19px; color: var(--ink); }

  .service-tag { position: absolute; left: 45px; top: 743px; width: 222px; height: 31px; border: 1.5px solid var(--brand-blue); display: flex; align-items: center; justify-content: center; font-family: 'Lato', sans-serif; font-weight: 400; font-size: 15.5px; color: var(--brand-orange); }

  .slogan { position: absolute; left: 0; right: 0; top: 296px; text-align: center; font-family: 'Oswald', sans-serif; font-weight: 700; color: var(--paper); text-transform: uppercase; line-height: 1; }
  .slogan__big { display: block; font-size: 36px; }
  .slogan__mid { display: block; font-size: 27px; margin: 1px 0 2px; }

  .product-list { position: absolute; left: 0; right: 0; top: 0; list-style: none; }
  .product { position: absolute; left: 22px; display: flex; align-items: center; gap: 16px; }
  .product__thumb { width: 77px; height: 77px; flex: none; }
  .product__label { font-family: 'Oswald', sans-serif; font-weight: 600; font-size: 21px; color: var(--brand-orange); text-transform: uppercase; letter-spacing: 0.2px; }

  .contact-cta { position: absolute; top: 788px; height: 34px; width: 148px; border-radius: 17px; background: var(--brand-orange); color: var(--paper); font-family: 'Lato', sans-serif; font-weight: 400; font-size: 20px; text-align: center; line-height: 26px; }
  .hanger--front .contact-cta { left: 78px; }
  .hanger--back .contact-cta { left: 79px; }

  .contact-band { position: absolute; left: 0; right: 0; top: 811px; bottom: 0; background: var(--brand-blue); color: var(--paper); font-family: 'Lato', sans-serif; font-weight: 700; font-size: 11.5px; padding: 10px 0 0 42px; }
  .contact-row { display: flex; align-items: flex-start; gap: 7px; line-height: 12px; margin-bottom: 9px; }
  .contact-row svg { flex: none; width: 10px; height: 10px; margin-top: 1px; }
  .contact-row .sep { margin: 0 5px; }
  .contact-row .inline-icon { display: inline-flex; align-items: center; gap: 4px; }
</style>
</head>
<body>
<main class="canvas">

  <!-- Front side -->
  <section class="hanger hanger--front" aria-label="Door hanger front">
    <svg class="hanger__bg" width="327" height="900" viewBox="0 0 327 900">
      <rect width="327" height="900" fill="var(--brand-blue)"/>
      <polygon points="0,414 327,486 327,900 0,900" fill="var(--paper)"/>
      <circle cx="165" cy="130" r="66" fill="var(--stage)"/>
    </svg>

    <div class="brand"><span class="brand__mark"></span><span class="brand__name">LEDGE CRAFTS</span></div>

    <svg class="hero-photo" width="327" height="900" viewBox="0 0 327 900">
      <defs>
        <radialGradient id="wallPanelTone" cx="45%" cy="45%" r="60%">
          <stop offset="0%" stop-color="#5a4d44"/>
          <stop offset="100%" stop-color="var(--photo-dark)"/>
        </radialGradient>
      </defs>
      <circle cx="165" cy="438" r="128" fill="var(--brand-orange)"/>
      <circle cx="158" cy="450" r="123" fill="var(--paper)"/>
      <circle cx="158" cy="450" r="119" fill="url(#wallPanelTone)" role="img" aria-label="Photo of a dark wall with square panel moulding and a dining chair"/>
    </svg>

    <h1 class="headline headline--front">
      <span class="headline__line headline__blue">Moulding Factory</span>
      <span class="headline__line headline__orange">Outlet Direct Sale</span>
    </h1>

    <p class="supply-copy">Supply High Quality Crown Mouldings, Baseboards, Casings and Wainscotings with Competitive Price</p>

    <div class="service-tag">INSTALLATION &amp; DELIVERY</div>

    <div class="contact-cta">Contact Us</div>
    <div class="contact-band">
      <div class="contact-row">
        <svg viewBox="0 0 10 10"><path d="M5 0.5a3.3 3.3 0 0 0-3.3 3.3C1.7 6.2 5 9.5 5 9.5s3.3-3.3 3.3-5.7A3.3 3.3 0 0 0 5 0.5z" fill="currentColor"/><circle cx="5" cy="3.8" r="1.2" fill="var(--brand-blue)"/></svg>
        <span>47 West Falcon Ridge Rd, Richmond Hill,<br>ON L4C 2H8</span>
      </div>
      <div class="contact-row">
        <svg viewBox="0 0 10 10"><circle cx="5" cy="5" r="4.3" fill="none" stroke="currentColor" stroke-width="0.9"/><path d="M3.5 3c.3 1.6 1.4 2.9 3 3.5l.5-.7-.9-.5-.4.4c-.6-.3-1-.8-1.3-1.4l.4-.4-.5-.9z" fill="currentColor"/></svg>
        <span>416 555 0143 | 416 555 0178</span>
      </div>
      <div class="contact-row">
        <svg viewBox="0 0 10 10"><rect x="0.5" y="2" width="9" height="6" fill="currentColor"/><path d="M0.5 2l4.5 3.5L9.5 2" fill="none" stroke="var(--brand-blue)" stroke-width="0.8"/></svg>
        <span>info@ledgecrafts.ca<span class="sep">|</span><span class="inline-icon"><svg viewBox="0 0 10 10" width="10" height="10"><circle cx="5" cy="5" r="4.2" fill="none" stroke="currentColor" stroke-width="0.8"/><ellipse cx="5" cy="5" rx="1.8" ry="4.2" fill="none" stroke="currentColor" stroke-width="0.7"/><path d="M0.8 5h8.4" stroke="currentColor" stroke-width="0.7"/></svg>ledgecrafts.ca</span></span>
      </div>
    </div>
  </section>

  <!-- Back side -->
  <section class="hanger hanger--back" aria-label="Door hanger back">
    <svg class="hanger__bg" width="327" height="900" viewBox="0 0 327 900">
      <rect width="327" height="900" fill="var(--brand-blue)"/>
      <polygon points="0,386 327,458 327,900 0,900" fill="var(--brand-orange)"/>
      <polygon points="0,395 327,467 327,900 0,900" fill="var(--paper)"/>
      <circle cx="165" cy="130" r="66" fill="var(--stage)"/>
    </svg>

    <div class="brand"><span class="brand__mark"></span><span class="brand__name">LEDGE CRAFTS</span></div>

    <h2 class="slogan">
      <span class="slogan__big">Convert Plain</span>
      <span class="slogan__mid">Room into Designer’s</span>
      <span class="slogan__big">Interiors</span>
    </h2>

    <ul class="product-list">
      <li class="product" style="top:440px">
        <svg class="product__thumb" viewBox="0 0 77 77" role="img" aria-label="Wainscoting moulding profile photo">
          <circle cx="38.5" cy="38.5" r="34" fill="var(--photo-light)"/>
          <path d="M4.5 38.5a34 34 0 0 1 68 0" fill="none" stroke="var(--brand-orange)" stroke-width="3"/>
          <path d="M72.5 38.5a34 34 0 0 1-68 0" fill="none" stroke="var(--brand-blue)" stroke-width="3"/>
        </svg>
        <span class="product__label">Wainscoting Walls</span>
      </li>
      <li class="product" style="top:526px">
        <svg class="product__thumb" viewBox="0 0 77 77" role="img" aria-label="Feature wall trim strip photo">
          <circle cx="38.5" cy="38.5" r="34" fill="var(--photo-light)"/>
          <path d="M4.5 38.5a34 34 0 0 1 68 0" fill="none" stroke="var(--brand-orange)" stroke-width="3"/>
          <path d="M72.5 38.5a34 34 0 0 1-68 0" fill="none" stroke="var(--brand-blue)" stroke-width="3"/>
        </svg>
        <span class="product__label">Feature Walls</span>
      </li>
      <li class="product" style="top:614px">
        <svg class="product__thumb" viewBox="0 0 77 77" role="img" aria-label="Flat stock board for waffle ceiling photo">
          <circle cx="38.5" cy="38.5" r="34" fill="var(--photo-light)"/>
          <path d="M4.5 38.5a34 34 0 0 1 68 0" fill="none" stroke="var(--brand-orange)" stroke-width="3"/>
          <path d="M72.5 38.5a34 34 0 0 1-68 0" fill="none" stroke="var(--brand-blue)" stroke-width="3"/>
        </svg>
        <span class="product__label">Waffle Ceiling</span>
      </li>
      <li class="product" style="top:702px">
        <svg class="product__thumb" viewBox="0 0 77 77" role="img" aria-label="Crown moulding profile photo">
          <circle cx="38.5" cy="38.5" r="34" fill="var(--photo-light)"/>
          <path d="M4.5 38.5a34 34 0 0 1 68 0" fill="none" stroke="var(--brand-orange)" stroke-width="3"/>
          <path d="M72.5 38.5a34 34 0 0 1-68 0" fill="none" stroke="var(--brand-blue)" stroke-width="3"/>
        </svg>
        <span class="product__label">Crown Mouldings</span>
      </li>
    </ul>

    <div class="contact-cta">Contact Us</div>
    <div class="contact-band">
      <div class="contact-row">
        <svg viewBox="0 0 10 10"><path d="M5 0.5a3.3 3.3 0 0 0-3.3 3.3C1.7 6.2 5 9.5 5 9.5s3.3-3.3 3.3-5.7A3.3 3.3 0 0 0 5 0.5z" fill="currentColor"/><circle cx="5" cy="3.8" r="1.2" fill="var(--brand-blue)"/></svg>
        <span>47 West Falcon Ridge Rd, Richmond Hill,<br>ON L4C 2H8</span>
      </div>
      <div class="contact-row">
        <svg viewBox="0 0 10 10"><circle cx="5" cy="5" r="4.3" fill="none" stroke="currentColor" stroke-width="0.9"/><path d="M3.5 3c.3 1.6 1.4 2.9 3 3.5l.5-.7-.9-.5-.4.4c-.6-.3-1-.8-1.3-1.4l.4-.4-.5-.9z" fill="currentColor"/></svg>
        <span>416 555 0143 | 416 555 0178</span>
      </div>
      <div class="contact-row">
        <svg viewBox="0 0 10 10"><rect x="0.5" y="2" width="9" height="6" fill="currentColor"/><path d="M0.5 2l4.5 3.5L9.5 2" fill="none" stroke="var(--brand-blue)" stroke-width="0.8"/></svg>
        <span>info@ledgecrafts.ca<span class="sep">|</span><span class="inline-icon"><svg viewBox="0 0 10 10" width="10" height="10"><circle cx="5" cy="5" r="4.2" fill="none" stroke="currentColor" stroke-width="0.8"/><ellipse cx="5" cy="5" rx="1.8" ry="4.2" fill="none" stroke="currentColor" stroke-width="0.7"/><path d="M0.8 5h8.4" stroke="currentColor" stroke-width="0.7"/></svg>ledgecrafts.ca</span></span>
      </div>
    </div>
  </section>

</main>
</body>
</html>
```